Combining 2 Websites into 1 Website

Hi, we are merging our 2 business websites into 1 website. A little bit our business. We are a Wholesale Food Company (Kandel Vita PNG Ltd) with a number of retail businesses including a Deli Butchery/Bakery (named The Rowly Grill Hof) and Fast Food Restaurants (Condor Stack, Tok Tam Rol, Gulpers) and a catering company called Rowly Dano Catering. At our head office (Kandel Vita) we also have 2 manufacturing factories - Bakery (Rowly Crust Hof products) and Butchery (Rowly Fine products).
Our current websites are:
- www.kandelvitapng.example (mother company)
- www.grillhof.example
We are looking to put all our brands under one website, with url www.kvz.example . The new website will contain the following pages:
www.kvz.example (home page)
About Us (similar look to our Kandel Vita Company Profile attached)
Contact (for Kandel Vita head office/sales)
All retail brand logos (click on a logo and be taken to that brands page)
www.kvz.example/grillhof
o Location
o Contact
o Order Online
www.kvz.example/condorstack
o Locations
o Contacts
o Order Online
www.kvz.example/toktamrol
o Location
o Contact
www.kvz.example/gulpers
o Location
o Contact
o Order Online
www.kvz.example/rowlydanocatering
o Location
o Contact
www.kvz.example/careers
o Information on how to apply for a job
o E-form that applicants complete and upload any paperwork to be sent to us? Name, DOB, Current Address, Phone Number, upload SV and Cover Letter
www.kvz.example/shoponline
All online retails will link to this page to do an online orders (like we have setup on our Grill Hof page). Only complexity is that Delivery Charge will need to be seperate for Grill Hof products vs Condor Stack / Gulpers products.
Information for the Kandel Vita home page can be found on the attached company Profile. Information (contact, location ect) can be found on our existing Grill Hof web page).
I have attached each of our logos. I have also attached a tribal fish design (pdf) which we use on all business cards, email signatures and uniforms across all sites. Logos include (all .png files):
- Kandel Vita Logo
- Grill Hof Logo
- Condor Stack Logo
- Gulpers Logo
- Tok Tam Rol Logo
- Rowly Dano Catering Logo
- Crust Hof Logo (for Kandel Vita - Bakery Factory Products)
- Rowly Fine logo (for Kandel Vita - Butchery Factory Products)
- QLSTM logo (Quality Assurance cert of our Butchery Factory)
Modern, Fun, Corporate
Food - Manufacturing, Wholesale & Delivery, Retail, Restaurants, Catering
Coded - Design and coding required
5+ page

```html
<!DOCTYPE html>
<html lang="en">
<head>
<meta charset="utf-8">
<title>Kandel Vita PNG Ltd – Website Pages</title>
<link href="https://fonts.googleapis.com/css2?family=Poppins:wght@400;500;600;700&display=swap" rel="stylesheet">
<style>
:root{
  --red:#ec1c24;
  --dark:#2e2e2e;
  --ink:#1f1f1f;
  --muted:#6b6b6b;
  --cream:#f5f3ee;
  --sheet:#bdbdbd;
  --white:#ffffff;
  --neutral:#d9d9d9;
}
*{box-sizing:border-box;margin:0;padding:0}
html,body{width:1200px;height:2321px;overflow:hidden}
body{background:var(--sheet);font-family:"Poppins",sans-serif;color:var(--ink);position:relative}
.page{position:absolute;background:var(--white);overflow:hidden}
.abs{position:absolute}
.topbar{position:absolute;top:0;right:0;background:var(--red);color:#fff;display:flex;align-items:center;justify-content:space-around;clip-path:polygon(10px 0,100% 0,100% 100%,0 100%);font-size:4px;padding-left:14px}
.topbar .phone{font-size:6px;font-weight:500}
.topbar svg{width:5px;height:5px;vertical-align:-1px;margin-right:2px}
.logo{position:absolute;color:var(--red);font-weight:700;font-size:11px;letter-spacing:-.2px;white-space:nowrap}
.nav{position:absolute;display:flex;align-items:center;font-size:4.1px;font-weight:500;letter-spacing:.1px}
.nav span{white-space:nowrap}
.nav .on{color:var(--red)}
.nav svg{width:6px;height:6px}
.ph{position:absolute}
.sec-title{position:absolute;left:0;right:0;text-align:center;font-weight:600}
.small{font-size:3.6px;line-height:1.55;color:var(--muted)}
.prod{position:absolute;display:flex;flex-direction:column;align-items:center;text-align:center}
.prod .ph{position:relative;width:100%}
.prod-name{font-size:5px;margin-top:6px;color:var(--ink)}
.prod-price{font-size:4.4px;color:var(--red);margin-top:1px}
.btn-cart{margin-top:4px;background:var(--red);color:#fff;font-size:3.8px;padding:2px 6px;border-radius:2px;box-shadow:0 0 0 1px #f6a8ab}
.more{position:absolute;left:0;right:0;text-align:center;color:var(--red);font-size:3.8px}
.footer{position:absolute;left:0;right:0;bottom:0;background:var(--dark);color:#fff}
.contact-card{position:absolute;background:var(--red);color:#fff;border-radius:8px;padding:14px 16px;font-size:3.8px;line-height:1.5}
.contact-card .big{font-size:9px;font-weight:500}
.contact-card b{font-weight:600}
.contact-card svg{width:6px;height:6px;vertical-align:-1px;margin-right:2px}
.hours{position:absolute;font-size:3.8px;line-height:1.5}
.hours b{font-weight:600}
.links{position:absolute;font-size:4px;line-height:2.1}
.copy{position:absolute;font-size:3.6px;color:#e0e0e0}
.hero-text{color:#fff}
.about-card{position:absolute;background:#fff;box-shadow:0 2px 8px rgba(0,0,0,.18);display:flex}
.why-item{position:absolute;width:88px;color:#fff}
.why-item h4{font-size:5.2px;font-weight:600;margin:3px 0 4px}
.why-item p{font-size:3.5px;line-height:1.55}
.why-item svg{width:7px;height:7px}
.brand-card{position:absolute;width:47px;height:58px;background:#fff;box-shadow:0 1px 5px rgba(0,0,0,.18);display:flex;flex-direction:column;align-items:center;justify-content:center;text-align:center}
.brand-card .mark{width:16px;height:16px;border-radius:50%;background:var(--neutral);margin-bottom:4px}
.brand-card .name{font-size:4.2px;font-weight:500;line-height:1.2;color:var(--muted)}
.brand-card .lm{font-size:3.4px;color:var(--red);margin-top:6px}
.job{position:absolute;width:101px;height:38px;background:#fff;box-shadow:0 1px 5px rgba(0,0,0,.18);display:flex;align-items:center;justify-content:center;text-align:center;font-size:5px;font-weight:600;line-height:1.2}
.field-label{position:absolute;color:#fff;font-size:3.8px}
.field{position:absolute;background:#fff;height:14px}
.cat{position:absolute;font-size:4.6px;color:#333;display:flex;align-items:center}
.cat i{display:inline-block;width:4px;height:4px;border:.5px solid #bbb;margin-right:4px}
</style>
</head>
<body>

<!-- ============ HOME PAGE ============ -->
<section class="page" style="left:60px;top:120px;width:444px;height:1222px">
  <div class="topbar" style="left:104px;height:19px">
    <span><svg viewBox="0 0 10 10"><path d="M5 0a3.5 3.5 0 0 0-3.5 3.5C1.5 6 5 10 5 10s3.5-4 3.5-6.5A3.5 3.5 0 0 0 5 0z" fill="#fff"/></svg>Sec 88, Lot 12-14, Harbour Road</span>
    <span><svg viewBox="0 0 10 10"><rect x="0.5" y="2" width="9" height="6" fill="none" stroke="#fff"/><path d="M.5 2 5 5.5 9.5 2" fill="none" stroke="#fff"/></svg>sales@kandelvitapng.example</span>
    <span class="phone"><svg viewBox="0 0 10 10"><path d="M2 1l2 2-1 1.5c.7 1.3 1.7 2.3 3 3L7.5 6.5l2 2L8 10C4 9.5.5 6 0 2z" fill="#fff"/></svg>3254700</span>
  </div>
  <div class="logo" style="left:24px;top:21px">Kandel Vita</div>
  <nav class="nav" style="left:90px;top:34px;gap:10px">
    <span class="on">HOME</span><span>GRILLHOF</span><span>CONDORSTACK</span><span>TOKTAMROL</span><span>GULPERS</span><span>ROWLYDANOCATERING</span><span>CAREERS</span><span>SHOP</span>
    <svg viewBox="0 0 10 10"><path d="M0 1h2l1.5 5h5L10 2.5H3" fill="none" stroke="#222" stroke-width=".8"/><circle cx="4" cy="8.5" r=".8" fill="#222"/><circle cx="8" cy="8.5" r=".8" fill="#222"/></svg>
    <svg viewBox="0 0 10 10"><circle cx="5" cy="3" r="2.2" fill="none" stroke="#222" stroke-width=".8"/><path d="M1 10c0-3 2-4.5 4-4.5s4 1.5 4 4.5" fill="none" stroke="#222" stroke-width=".8"/></svg>
  </nav>

  <div class="ph" role="img" aria-label="Dark slate background with raw cuts of meat on a wooden board" style="left:0;top:49px;width:444px;height:218px;background:linear-gradient(90deg,#151515 0%,#2b2b2b 45%,#3a2522 62%,#7e2b2b 80%,#2a2222 100%)"></div>
  <div class="abs" style="left:325px;top:66px;color:var(--red);font-weight:700;font-size:11px;line-height:.95">FRESH &amp;<br>AUTHENTIC</div>
  <div class="abs hero-text" style="left:66px;top:98px;font-size:9.5px;font-weight:500">ROWLY HOF</div>
  <div class="abs hero-text" style="left:65px;top:111px;font-size:27px;font-weight:600;letter-spacing:.3px">GRILL HOF</div>
  <div class="abs hero-text" style="left:66px;top:145px;font-size:10.5px;line-height:1.3">Experience the grill hof<br>Quality,Service and value</div>
  <svg class="abs" style="left:35px;top:143px" width="15" height="15" viewBox="0 0 20 20"><circle cx="10" cy="10" r="10" fill="var(--red)"/><path d="M12 5 7 10l5 5" fill="none" stroke="#fff" stroke-width="2"/></svg>
  <svg class="abs" style="left:404px;top:143px" width="15" height="15" viewBox="0 0 20 20"><circle cx="10" cy="10" r="10" fill="var(--red)"/><path d="M8 5l5 5-5 5" fill="none" stroke="#fff" stroke-width="2"/></svg>

  <div class="about-card" style="left:47px;top:227px;width:353px;height:168px">
    <div class="ph" role="img" aria-label="Fresh salmon, prawns and fish on ice" style="position:relative;width:180px;height:100%;background:linear-gradient(135deg,#6d8ea0 0%,#d9dfe2 35%,#e5835a 60%,#c9663f 80%,#8ea3ad 100%)"></div>
    <div style="padding:26px 14px 0 22px;flex:1">
      <div style="font-size:5.6px;font-weight:600;margin-bottom:6px">About Us</div>
      <p class="small" style="margin-bottom:6px">Kandel Vita PNG has been operating since 2011. The company is family run and guided by owners with deep roots in PNG. For more than 30 years they have lived and worked across the highlands, the islands and central PNG.</p>
      <p class="small">Kandel Vita PNG has been operating since 2011. The company is family run and guided by owners with deep roots in PNG. For more than 30 years they have lived and worked across the highlands, the islands and central PNG.</p>
      <div style="display:flex;gap:10px;margin-top:14px;align-items:center">
        <span style="width:24px;height:9px;background:var(--neutral);border-radius:2px"></span>
        <span style="width:30px;height:9px;background:var(--neutral);border-radius:2px"></span>
        <span style="width:26px;height:9px;background:var(--neutral);border-radius:2px"></span>
      </div>
    </div>
  </div>

  <div class="abs" style="left:0;top:415px;width:444px;height:279px;background:var(--red)"></div>
  <div class="sec-title" style="top:450px;color:#fff;font-size:9px">Why Choose Us</div>
  <div class="why-item" style="left:47px;top:502px"><svg viewBox="0 0 10 10"><circle cx="5" cy="3" r="2.3" fill="#fff"/><path d="M1 10c0-3 2-4.5 4-4.5s4 1.5 4 4.5z" fill="#fff"/></svg><h4>Experience</h4><p>Kandel Vita PNG has served the country since 2011. The family team has lived and worked in PNG for more than 30 years, across the highlands, the islands and central regions.</p></div>
  <div class="why-item" style="left:181px;top:502px"><svg viewBox="0 0 10 10"><rect x="1" y="4" width="8" height="6" fill="#fff"/><path d="M0 4.5 5 0l5 4.5z" fill="#fff"/></svg><h4>Storage &amp; Infrastructure</h4><p>Kandel Vita PNG has served the country since 2011. The family team has lived and worked in PNG for more than 30 years, across the highlands, the islands and central regions.</p></div>
  <div class="why-item" style="left:308px;top:502px"><svg viewBox="0 0 10 10"><rect x="0" y="2" width="6" height="5" fill="#fff"/><path d="M6 4h2.5L10 6v1H6z" fill="#fff"/><circle cx="2" cy="8.5" r="1.2" fill="#fff"/><circle cx="8" cy="8.5" r="1.2" fill="#fff"/></svg><h4>Transport</h4><p>Kandel Vita PNG has served the country since 2011. The family team has lived and worked in PNG for more than 30 years, across the highlands, the islands and central regions.</p></div>
  <div class="why-item" style="left:47px;top:595px"><svg viewBox="0 0 10 10"><path d="M5 0 9 1.5V5c0 2.5-2 4.2-4 5-2-.8-4-2.5-4-5V1.5z" fill="#fff"/></svg><h4>Health &amp; Safety</h4><p>Kandel Vita PNG has served the country since 2011. The family team has lived and worked in PNG for more than 30 years, across the highlands, the islands and central regions.</p></div>
  <div class="why-item" style="left:181px;top:595px"><svg viewBox="0 0 10 10"><circle cx="3" cy="3" r="2" fill="#fff"/><circle cx="7.5" cy="4" r="1.6" fill="#fff"/><path d="M0 10c0-3 1.5-4 3-4s3 1 3 4zM5.5 10c0-2.5 1-3.5 2-3.5S10 7.5 10 10z" fill="#fff"/></svg><h4>Suppliers</h4><p>Kandel Vita PNG has served the country since 2011. The family team has lived and worked in PNG for more than 30 years, across the highlands, the islands and central regions.</p></div>
  <div class="why-item" style="left:308px;top:595px"><svg viewBox="0 0 10 10"><circle cx="5" cy="2" r="1.6" fill="#fff"/><circle cx="2" cy="4" r="1.4" fill="#fff"/><circle cx="8" cy="4" r="1.4" fill="#fff"/><rect x="0" y="6" width="10" height="4" rx="1" fill="#fff"/></svg><h4>People</h4><p>Kandel Vita PNG has served the country since 2011. The family team has lived and worked in PNG for more than 30 years, across the highlands, the islands and central regions.</p></div>

  <div class="sec-title" style="top:719px;font-size:8.5px">Retails Brands</div>
  <div class="brand-card" style="left:77px;top:747px"><div class="mark"></div><div class="name">Grill Hof</div><div class="lm">Learn more »</div></div>
  <div class="brand-card" style="left:132px;top:747px"><div class="mark"></div><div class="name">Condor Stack</div><div class="lm">Learn more »</div></div>
  <div class="brand-card" style="left:187px;top:747px"><div class="mark"></div><div class="name">Rowly Dano</div><div class="lm">Learn more »</div></div>
  <div class="brand-card" style="left:241px;top:747px"><div class="mark"></div><div class="name">Tok Tam Rol</div><div class="lm">Learn more »</div></div>
  <div class="brand-card" style="left:296px;top:747px"><div class="mark"></div><div class="name">Gulpers</div><div class="lm">Learn more »</div></div>

  <div class="abs" style="left:0;top:841px;width:444px;height:266px;background:var(--cream)"></div>
  <div class="sec-title" style="top:865px;color:var(--red);font-size:9.5px">Shop</div>
  <div class="prod" style="left:47px;top:891px;width:81px"><div class="ph" role="img" aria-label="Fried chicken pieces with chips" style="height:81px;background:linear-gradient(135deg,#1e1a17,#8a5a2a 55%,#c98a3e)"></div><div class="prod-name">3 Pc Chicken</div><div class="prod-price">K30.00</div><div class="btn-cart">ADD TO CART</div></div>
  <div class="prod" style="left:140px;top:891px;width:81px"><div class="ph" role="img" aria-label="Bag of hamburger rolls" style="height:81px;background:linear-gradient(180deg,#fff 0%,#efe6da 40%,#d8b98e 70%,#8a1e1e 100%)"></div><div class="prod-name">Hamburger Rolls 6 Pack</div><div class="prod-price">K8.25</div><div class="btn-cart">ADD TO CART</div></div>
  <div class="prod" style="left:231px;top:891px;width:81px"><div class="ph" role="img" aria-label="Cheesy pizza loaf" style="height:81px;background:radial-gradient(ellipse at center,#e0a848 0%,#d58a2e 40%,#fff 72%)"></div><div class="prod-name">Pizza Loaf</div><div class="prod-price">K10.99</div><div class="btn-cart">ADD TO CART</div></div>
  <div class="prod" style="left:322px;top:891px;width:81px"><div class="ph" role="img" aria-label="Raw lamb french cutlets" style="height:81px;background:linear-gradient(135deg,#4a3022,#b04848 55%,#e0a0a0)"></div><div class="prod-name">French Cutlets 500g</div><div class="prod-price">K67.78</div><div class="btn-cart">ADD TO CART</div></div>
  <div class="more" style="top:1045px">SHOP MORE PRODUCTS →</div>

  <div class="footer" style="height:115px">
    <div class="hours" style="left:49px;top:16px"><b>Trading Hours</b><br>Monday - Friday<br>8AM - 4:30PM<br><br>Saturday<br>8AM - 12PM<br><br>Sunday<br>CLOSED</div>
    <div class="links" style="left:262px;top:17px">Terms &amp; Conditions<br>Privacy Policy<br>FAQ<br>In-Store Pick-up Info</div>
    <div class="links" style="left:337px;top:17px">Shop Online<br>My Account<br>Careers<br>Contact Us</div>
    <div class="copy" style="left:49px;top:98px">©2022 COPYRIGHT KANDEL VITA PNG LTD. ALL RIGHTS RESERVED.</div>
  </div>
  <div class="contact-card" style="left:118px;top:1081px;width:109px;height:103px;padding:12px 14px">
    Contact us today<br><span class="big">✆ 3254700</span><br><br><b>Email</b><br><svg viewBox="0 0 10 10"><rect x=".5" y="2" width="9" height="6" fill="none" stroke="#fff"/><path d="M.5 2 5 5.5 9.5 2" fill="none" stroke="#fff"/></svg>sales@kandelvitapng.example<br><br><b>Location</b><br>Sec 88, Lot 12-14<br>Harbour Road<br>KOKI BAY, PNG
  </div>
</section>

<!-- ============ GRILL HOF PAGE ============ -->
<section class="page" style="left:600px;top:120px;width:529px;height:917px">
  <div class="topbar" style="left:124px;height:22px;font-size:4.6px">
    <span><svg viewBox="0 0 10 10"><path d="M5 0a3.5 3.5 0 0 0-3.5 3.5C1.5 6 5 10 5 10s3.5-4 3.5-6.5A3.5 3.5 0 0 0 5 0z" fill="#fff"/></svg>Sec 88, Lot 12-14, Harbour Road</span>
    <span><svg viewBox="0 0 10 10"><rect x=".5" y="2" width="9" height="6" fill="none" stroke="#fff"/><path d="M.5 2 5 5.5 9.5 2" fill="none" stroke="#fff"/></svg>sales@kandelvitapng.example</span>
    <span class="phone" style="font-size:7px">✆ 3254700</span>
  </div>
  <div class="logo" style="left:30px;top:26px;font-size:13px">Kandel Vita</div>
  <nav class="nav" style="left:124px;top:40px;gap:13px;font-size:4.6px">
    <span class="on">HOME</span><span>GRILLHOF</span><span>CONDORSTACK</span><span>TOKTAMROL</span><span>GULPERS</span><span>ROWLYDANOCATERING</span><span>CAREERS</span><span>SHOP</span>
    <svg viewBox="0 0 10 10"><path d="M0 1h2l1.5 5h5L10 2.5H3" fill="none" stroke="#222" stroke-width=".8"/><circle cx="4" cy="8.5" r=".8" fill="#222"/><circle cx="8" cy="8.5" r=".8" fill="#222"/></svg>
    <svg viewBox="0 0 10 10"><circle cx="5" cy="3" r="2.2" fill="none" stroke="#222" stroke-width=".8"/><path d="M1 10c0-3 2-4.5 4-4.5s4 1.5 4 4.5" fill="none" stroke="#222" stroke-width=".8"/></svg>
  </nav>

  <div class="abs" style="left:0;top:54px;width:529px;height:154px;background:var(--cream)"></div>
  <div class="ph" role="img" aria-label="Grill Hof banner with raw steak and spices" style="left:64px;top:87px;width:245px;height:82px;background:linear-gradient(90deg,#7a1418 0%,#c8242a 35%,#5a1a1a 65%,#2a1a16 100%)"></div>
  <div class="abs" style="left:324px;top:92px;color:var(--red);font-size:10px;font-weight:600">Grill Hof</div>
  <p class="abs small" style="left:324px;top:109px;width:155px;font-size:4px;color:#444">Delicious Burgers, Fried Chicken, Chips, Milkshakes and more. There are 3 stores in Port Moresby, located at Central, Town and Hilltop (Park Retail Village).</p>

  <div class="abs" style="left:46px;top:222px;width:200px">
    <div style="font-size:5.6px;font-weight:600">Location</div>
    <p class="small" style="font-size:4px;color:#444;margin-top:3px">CENTRAL STORE</p>
    <p class="small" style="font-size:4px;color:#444;margin-top:4px">Our largest Grill Hof store, with a Condor Stack Takeaway Restaurant attached.</p>
    <p class="small" style="font-size:4px;color:#444;margin-top:6px">Located inside a secure compound on the corner of Kesi Rd and Central Drive (same compound as Harbour Bank, opposite Ridge Motors). The compound also includes our Rowly Dano Catering office. The compound has ample secure parking.</p>
  </div>
  <div class="ph" role="img" aria-label="Street map of the store location" style="left:46px;top:317px;width:198px;height:81px;background:linear-gradient(135deg,#e8ecef,#d5dde3 50%,#e9e6df)"></div>
  <div class="abs" style="left:326px;top:229px;width:160px">
    <div style="font-size:5.6px;font-weight:600">Contact</div>
    <p class="small" style="font-size:4px;color:#444;margin-top:4px">(+675) 7000 4821<br>Email: grillhof@kandelvitapng.example</p>
    <p class="small" style="font-size:4px;color:#444;margin-top:5px">Rowly Grill Hof Central<br>MONDAY to THU: 8:00am – 6:30pm<br>FRI: 8:00am – 6:30pm<br>SAT &amp; SUN: 8:00am - 5:00pm</p>
  </div>
  <div class="abs" style="left:46px;top:431px;width:430px;height:1px;background:#ccc"></div>

  <div class="sec-title" style="top:464px;font-size:10.5px;font-weight:500">Grillhof Products</div>
  <div class="prod" style="left:53px;top:502px;width:96px"><div class="ph" role="img" aria-label="Fried chicken pieces with chips" style="height:95px;background:linear-gradient(135deg,#1e1a17,#8a5a2a 55%,#c98a3e)"></div><div class="prod-name" style="font-size:5.8px">3 Pc Chicken</div><div class="prod-price" style="font-size:5px">K30.00</div><div class="btn-cart" style="font-size:4.2px">ADD TO CART</div></div>
  <div class="prod" style="left:163px;top:502px;width:96px"><div class="ph" role="img" aria-label="Bag of hamburger rolls" style="height:95px;background:linear-gradient(180deg,#fff 0%,#efe6da 40%,#d8b98e 70%,#8a1e1e 100%)"></div><div class="prod-name" style="font-size:5.8px">Hamburger Rolls 6 Pack</div><div class="prod-price" style="font-size:5px">K8.25</div><div class="btn-cart" style="font-size:4.2px">ADD TO CART</div></div>
  <div class="prod" style="left:273px;top:502px;width:96px"><div class="ph" role="img" aria-label="Cheesy pizza loaf" style="height:95px;background:radial-gradient(ellipse at center,#e0a848 0%,#d58a2e 40%,#fff 72%)"></div><div class="prod-name" style="font-size:5.8px">Pizza Loaf</div><div class="prod-price" style="font-size:5px">K10.99</div><div class="btn-cart" style="font-size:4.2px">ADD TO CART</div></div>
  <div class="prod" style="left:380px;top:502px;width:96px"><div class="ph" role="img" aria-label="Raw lamb french cutlets" style="height:95px;background:linear-gradient(135deg,#4a3022,#b04848 55%,#e0a0a0)"></div><div class="prod-name" style="font-size:5.8px">French Cutlets 500g</div><div class="prod-price" style="font-size:5px">K67.78</div><div class="btn-cart" style="font-size:4.2px">ADD TO CART</div></div>
  <div class="more" style="top:688px">SHOP MORE GRILLHOF PRODUCT →</div>

  <div class="footer" style="height:139px">
    <div class="hours" style="left:58px;top:21px;font-size:4.2px"><b>Trading Hours</b><br><br>Monday - Friday<br><b>8AM - 4:30PM</b><br><br>Saturday<br><b>8AM - 12PM</b><br><br>Sunday<br><b>CLOSED</b></div>
    <div class="links" style="left:311px;top:26px;font-size:4.4px">Terms &amp; Conditions<br>Privacy Policy<br>FAQ<br>In-Store Pick-up Info</div>
    <div class="links" style="left:401px;top:26px;font-size:4.4px">Shop Online<br>My Account<br>Careers<br>Contact Us</div>
    <div class="copy" style="left:58px;top:119px;font-size:4px">©2022 COPYRIGHT KANDEL VITA PNG LTD. ALL RIGHTS RESERVED.</div>
  </div>
  <div class="contact-card" style="left:140px;top:747px;width:129px;height:122px;padding:16px 30px;font-size:4.2px">
    Contact us today<br><span class="big" style="font-size:10px">✆ 3254700</span><br><br><b>Email</b><br><svg viewBox="0 0 10 10"><rect x=".5" y="2" width="9" height="6" fill="none" stroke="#fff"/><path d="M.5 2 5 5.5 9.5 2" fill="none" stroke="#fff"/></svg>sales@kandelvitapng.example<br><br><b>Location</b><br>Sec 88, Lot 12-14<br>Harbour Road<br>KOKI BAY, PNG
  </div>
</section>

<!-- ============ CAREERS PAGE ============ -->
<section class="page" style="left:60px;top:1402px;width:453px;height:785px">
  <div class="topbar" style="left:104px;height:18px">
    <span><svg viewBox="0 0 10 10"><path d="M5 0a3.5 3.5 0 0 0-3.5 3.5C1.5 6 5 10 5 10s3.5-4 3.5-6.5A3.5 3.5 0 0 0 5 0z" fill="#fff"/></svg>Sec 88, Lot 12-14, Harbour Road</span>
    <span><svg viewBox="0 0 10 10"><rect x=".5" y="2" width="9" height="6" fill="none" stroke="#fff"/><path d="M.5 2 5 5.5 9.5 2" fill="none" stroke="#fff"/></svg>sales@kandelvitapng.example</span>
    <span class="phone">✆ 3254700</span>
  </div>
  <div class="logo" style="left:24px;top:20px">Kandel Vita</div>
  <nav class="nav" style="left:102px;top:34px;gap:10px">
    <span class="on">HOME</span><span>GRILLHOF</span><span>CONDORSTACK</span><span>TOKTAMROL</span><span>GULPERS</span><span>ROWLYDANOCATERING</span><span>CAREERS</span><span>SHOP</span>
    <svg viewBox="0 0 10 10"><path d="M0 1h2l1.5 5h5L10 2.5H3" fill="none" stroke="#222" stroke-width=".8"/><circle cx="4" cy="8.5" r=".8" fill="#222"/><circle cx="8" cy="8.5" r=".8" fill="#222"/></svg>
    <svg viewBox="0 0 10 10"><circle cx="5" cy="3" r="2.2" fill="none" stroke="#222" stroke-width=".8"/><path d="M1 10c0-3 2-4.5 4-4.5s4 1.5 4 4.5" fill="none" stroke="#222" stroke-width=".8"/></svg>
  </nav>
  <div class="ph" role="img" aria-label="Leather briefcase held against a dark background" style="left:0;top:48px;width:453px;height:162px;background:linear-gradient(90deg,#3e4548 0%,#2c3134 40%,#1b1d1f 65%,#3a3f42 100%)"></div>
  <div class="sec-title" style="top:119px;color:#fff;font-size:15px;font-weight:500">Career</div>
  <p class="abs" style="left:80px;top:229px;width:293px;text-align:center;font-size:4px;line-height:1.6;color:#444">Kandel Vita PNG Ltd is a rapidly expanding organisation in Papua New Guinea. We specialise in Production, Wholesale, Retail and Delivery of fine foods to our valued clients. We are seeking suitably qualified, enthusiastic and reliable individuals to join our company. See below current opportunities.</p>
  <div class="sec-title" style="top:278px;color:var(--red);font-size:10.5px;font-weight:500">We are hiring</div>
  <div class="job" style="left:64px;top:302px">Administratuve and<br>Support Services</div>
  <div class="job" style="left:173px;top:302px">Driver &amp; Transportation</div>
  <div class="job" style="left:283px;top:302px">Accounting &amp; Finance</div>
  <div class="job" style="left:64px;top:347px">Human Resource</div>
  <div class="job" style="left:173px;top:347px">Merchandising</div>
  <div class="job" style="left:283px;top:347px">HR Management</div>

  <div class="abs" style="left:0;top:409px;width:453px;height:219px;background:var(--red)"></div>
  <div class="field-label" style="left:101px;top:442px">Name</div><div class="field" style="left:101px;top:450px;width:110px"></div>
  <div class="field-label" style="left:232px;top:442px">Phone</div><div class="field" style="left:232px;top:450px;width:110px"></div>
  <div class="field-label" style="left:101px;top:475px">Email</div><div class="field" style="left:101px;top:483px;width:110px"></div>
  <div class="field-label" style="left:232px;top:475px">DOB</div><div class="field" style="left:232px;top:483px;width:110px"></div>
  <div class="field-label" style="left:101px;top:508px">Address</div><div class="field" style="left:101px;top:517px;width:241px;height:30px"></div>
  <div class="field-label" style="left:101px;top:557px">Upload your SV &amp; COver Letter</div>
  <div class="abs" style="left:101px;top:566px;background:#fff;font-size:3.6px;padding:2px 6px">Select files</div>
  <div class="abs" style="left:292px;top:596px;width:49px;height:11px;background:#fff;color:var(--red);border-radius:6px;font-size:4.6px;display:flex;align-items:center;justify-content:center">SUBMIT</div>

  <div class="footer" style="height:118px">
    <div class="hours" style="left:49px;top:15px"><b>Trading Hours</b><br>Monday - Friday<br>8AM - 4:30PM<br><br>Saturday<br>8AM - 12PM<br><br>Sunday<br>CLOSED</div>
    <div class="links" style="left:266px;top:17px">Terms &amp; Conditions<br>Privacy Policy<br>FAQ<br>In-Store Pick-up Info</div>
    <div class="links" style="left:343px;top:17px">Shop Online<br>My Account<br>Careers<br>Contact Us</div>
    <div class="copy" style="left:55px;top:100px">©2022 COPYRIGHT KANDEL VITA PNG LTD. ALL RIGHTS RESERVED.</div>
  </div>
  <div class="contact-card" style="left:120px;top:639px;width:110px;height:106px;padding:13px 22px">
    Contact us today<br><span class="big">✆ 3254700</span><br><br><b>Email</b><br><svg viewBox="0 0 10 10"><rect x=".5" y="2" width="9" height="6" fill="none" stroke="#fff"/><path d="M.5 2 5 5.5 9.5 2" fill="none" stroke="#fff"/></svg>sales@kandelvitapng.example<br><br><b>Location</b><br>Sec 88, Lot 12-14<br>Harbour Road<br>KOKI BAY, PNG
  </div>
</section>

<!-- ============ SHOP PAGE ============ -->
<section class="page" style="left:600px;top:1070px;width:530px;height:798px">
  <div class="topbar" style="left:124px;height:22px;font-size:4.6px">
    <span><svg viewBox="0 0 10 10"><path d="M5 0a3.5 3.5 0 0 0-3.5 3.5C1.5 6 5 10 5 10s3.5-4 3.5-6.5A3.5 3.5 0 0 0 5 0z" fill="#fff"/></svg>Sec 88, Lot 12-14, Harbour Road</span>
    <span><svg viewBox="0 0 10 10"><rect x=".5" y="2" width="9" height="6" fill="none" stroke="#fff"/><path d="M.5 2 5 5.5 9.5 2" fill="none" stroke="#fff"/></svg>sales@kandelvitapng.example</span>
    <span class="phone" style="font-size:7px">✆ 3254700</span>
  </div>
  <div class="logo" style="left:30px;top:26px;font-size:13px">Kandel Vita</div>
  <nav class="nav" style="left:124px;top:40px;gap:13px;font-size:4.6px">
    <span class="on">HOME</span><span>GRILLHOF</span><span>CONDORSTACK</span><span>TOKTAMROL</span><span>GULPERS</span><span>ROWLYDANOCATERING</span><span>CAREERS</span><span>SHOP</span>
    <svg viewBox="0 0 10 10"><path d="M0 1h2l1.5 5h5L10 2.5H3" fill="none" stroke="#222" stroke-width=".8"/><circle cx="4" cy="8.5" r=".8" fill="#222"/><circle cx="8" cy="8.5" r=".8" fill="#222"/></svg>
    <svg viewBox="0 0 10 10"><circle cx="5" cy="3" r="2.2" fill="none" stroke="#222" stroke-width=".8"/><path d="M1 10c0-3 2-4.5 4-4.5s4 1.5 4 4.5" fill="none" stroke="#222" stroke-width=".8"/></svg>
  </nav>

  <div class="abs" style="left:32px;top:82px;font-size:5px;font-weight:600">Shop By Category</div>
  <div class="cat" style="left:32px;top:96px"><i></i>Bakery</div>
  <div class="cat" style="left:32px;top:109px"><i></i>Beef</div>
  <div class="cat" style="left:32px;top:123px"><i></i>Condor Stack</div>
  <div class="cat" style="left:41px;top:136px"><i></i>Condor Boxes</div>
  <div class="cat" style="left:41px;top:148px"><i></i>Burgers</div>
  <div class="cat" style="left:41px;top:160px"><i></i>Chips</div>
  <div class="cat" style="left:32px;top:174px"><i></i>Cakes</div>
  <div class="cat" style="left:32px;top:187px"><i></i>Dairy</div>
  <div class="cat" style="left:32px;top:200px"><i></i>Fruit &amp; Vegetables</div>
  <div class="cat" style="left:32px;top:213px"><i></i>Gift Vouchers</div>
  <div class="cat" style="left:32px;top:226px"><i></i>Hot Food</div>
  <div class="abs" style="left:32px;top:252px;font-size:5px;font-weight:600">Price</div>
  <div class="abs" style="left:32px;top:261px;width:40px;height:9px;border:.6px solid #bbb"></div>
  <div class="abs" style="left:77px;top:261px;width:40px;height:9px;border:.6px solid #bbb"></div>
  <div class="abs" style="left:34px;top:280px;width:81px;height:1.5px;background:var(--red)"></div>
  <div class="abs" style="left:32px;top:278px;width:5px;height:5px;border-radius:50%;background:#ccc"></div>
  <div class="abs" style="left:113px;top:278px;width:5px;height:5px;border-radius:50%;background:#ccc"></div>

  <div class="abs" style="left:159px;top:78px;font-size:12px;font-weight:500">Shop</div>
  <div class="abs" style="left:159px;top:102px;width:61px;height:10px;border:.6px solid #ccc;border-radius:5px;font-size:3.6px;color:#888;padding:2px 5px">Default sorting ⌄</div>
  <div class="abs" style="left:239px;top:104px;font-size:4px;color:#444">Showing 1–16 of 233 results</div>

  <div class="prod" style="left:159px;top:138px;width:75px"><div class="ph" role="img" aria-label="Fried chicken pieces with chips" style="height:75px;background:linear-gradient(135deg,#1e1a17,#8a5a2a 55%,#c98a3e)"></div><div class="prod-name">3 Pc Chicken</div><div class="prod-price">K30.00</div><div class="btn-cart">ADD TO CART</div></div>
  <div class="abs" style="left:159px;top:141px;background:var(--red);color:#fff;font-size:3.4px;padding:1px 3px">SAVE 15%</div>
  <div class="prod" style="left:245px;top:138px;width:75px"><div class="ph" role="img" aria-label="Bag of hamburger rolls" style="height:75px;background:linear-gradient(180deg,#fff 0%,#efe6da 40%,#d8b98e 70%,#8a1e1e 100%)"></div><div class="prod-name">Hamburger Rolls 6 Pack</div><div class="prod-price">K8.25</div><div class="btn-cart">ADD TO CART</div></div>
  <div class="prod" style="left:331px;top:138px;width:75px"><div class="ph" role="img" aria-label="Cheesy pizza loaf" style="height:75px;background:radial-gradient(ellipse at center,#e0a848 0%,#d58a2e 40%,#fff 72%)"></div><div class="prod-name">Pizza Loaf</div><div class="prod-price">K10.99</div><div class="btn-cart">ADD TO CART</div></div>
  <div class="prod" style="left:416px;top:138px;width:75px"><div class="ph" role="img" aria-label="Raw lamb french cutlets" style="height:75px;background:linear-gradient(135deg,#4a3022,#b04848 55%,#e0a0a0)"></div><div class="prod-name">French Cutlets 500g</div><div class="prod-price">K67.78</div><div class="btn-cart">ADD TO CART</div></div>

  <div class="prod" style="left:159px;top:279px;width:75px"><div class="ph" role="img" aria-label="Pack of sliced cheese" style="height:75px;background:linear-gradient(135deg,#fff,#f5c84a 50%,#d62a2a)"></div><div class="prod-name">3 Pc Chicken</div><div class="prod-price">K30.00</div><div class="btn-cart">ADD TO CART</div></div>
  <div class="prod" style="left:245px;top:279px;width:75px"><div class="ph" role="img" aria-label="Box of cream cheese" style="height:75px;background:linear-gradient(135deg,#fff,#2a5aa8 50%,#e8eef6)"></div><div class="prod-name">Hamburger Rolls 6 Pack</div><div class="prod-price">K8.25</div><div class="btn-cart">ADD TO CART</div></div>
  <div class="prod" style="left:331px;top:279px;width:75px"><div class="ph" role="img" aria-label="Raw beef steaks" style="height:75px;background:linear-gradient(135deg,#6a1e22,#b23a3e 55%,#7a2a2a)"></div><div class="prod-name">Pizza Loaf</div><div class="prod-price">K10.99</div><div class="btn-cart">ADD TO CART</div></div>
  <div class="prod" style="left:416px;top:279px;width:75px"><div class="ph" role="img" aria-label="Burger on a dark background" style="height:75px;background:radial-gradient(circle at center,#d9a15a 0%,#7a3a1e 35%,#151515 70%)"></div><div class="prod-name">French Cutlets 500g</div><div class="prod-price">K67.78</div><div class="btn-cart">ADD TO CART</div></div>

  <div class="prod" style="left:159px;top:426px;width:75px"><div class="ph" role="img" aria-label="Fresh broccoli" style="height:75px;background:linear-gradient(135deg,#6a8a3a,#2f6a2a 55%,#4a3a2a)"></div><div class="prod-name">3 Pc Chicken</div><div class="prod-price">K30.00</div><div class="btn-cart">ADD TO CART</div></div>
  <div class="prod" style="left:245px;top:426px;width:75px"><div class="ph" role="img" aria-label="Sausages on a board" style="height:75px;background:linear-gradient(135deg,#f0e6d8,#d98a6a 50%,#b86a4a)"></div><div class="prod-name">Hamburger Rolls 6 Pack</div><div class="prod-price">K8.25</div><div class="btn-cart">ADD TO CART</div></div>
  <div class="prod" style="left:331px;top:426px;width:75px"><div class="ph" role="img" aria-label="Cheesy pizza loaf" style="height:75px;background:radial-gradient(ellipse at center,#e0a848 0%,#d58a2e 40%,#fff 72%)"></div><div class="prod-name">Pizza Loaf</div><div class="prod-price">K10.99</div><div class="btn-cart">ADD TO CART</div></div>
  <div class="prod" style="left:416px;top:426px;width:75px"><div class="ph" role="img" aria-label="Raw lamb french cutlets" style="height:75px;background:linear-gradient(135deg,#4a3022,#b04848 55%,#e0a0a0)"></div><div class="prod-name">French Cutlets 500g</div><div class="prod-price">K67.78</div><div class="btn-cart">ADD TO CART</div></div>

  <div class="abs" style="left:461px;top:597px;display:flex;gap:4px;font-size:4px;align-items:center"><span style="background:#ddd;padding:0 2px">1</span><span>2</span><span>›</span></div>

  <div class="footer" style="height:139px">
    <div class="hours" style="left:58px;top:21px;font-size:4.2px"><b>Trading Hours</b><br><br>Monday - Friday<br><b>8AM - 4:30PM</b><br><br>Saturday<br><b>8AM - 12PM</b><br><br>Sunday<br><b>CLOSED</b></div>
    <div class="links" style="left:311px;top:26px;font-size:4.4px">Terms &amp; Conditions<br>Privacy Policy<br>FAQ<br>In-Store Pick-up Info</div>
    <div class="links" style="left:402px;top:26px;font-size:4.4px">Shop Online<br>My Account<br>Careers<br>Contact Us</div>
    <div class="copy" style="left:58px;top:119px;font-size:4px">©2022 COPYRIGHT KANDEL VITA PNG LTD. ALL RIGHTS RESERVED.</div>
  </div>
  <div class="contact-card" style="left:141px;top:628px;width:128px;height:124px;padding:16px 30px;font-size:4.2px">
    Contact us today<br><span class="big" style="font-size:10px">✆ 3254700</span><br><br><b>Email</b><br><svg viewBox="0 0 10 10"><rect x=".5" y="2" width="9" height="6" fill="none" stroke="#fff"/><path d="M.5 2 5 5.5 9.5 2" fill="none" stroke="#fff"/></svg>sales@kandelvitapng.example<br><br><b>Location</b><br>Sec 88, Lot 12-14<br>Harbour Road<br>KOKI BAY, PNG
  </div>
</section>

</body>
</html>
```